Label for Gin Bottle - Cranberry & Peach

Hi, We have created a Cranberry & Peach Gin that we require a label for.
The gin will be a vivid Orange/red colour in a clear 50cl bottle
The gin will be 40% Vol.
I am looking for a classy design with a summer/fresh appearance.
Thank You.

```html
<!DOCTYPE html>
<html lang="en">
<head>
<meta charset="UTF-8">
<title>Cranberry &amp; Peach Gin – Label</title>
<link rel="stylesheet" href="https://fonts.googleapis.com/css2?family=Cormorant+Garamond:wght@500;600&family=Open+Sans:wght@500&display=swap">
<style>
  :root {
    --page-bg: #e9edf3;
    --teal: #3f8a8a;
    --teal-light: #7fb7b5;
    --gin-red: #c9341c;
    --gin-deep: #8e1f12;
    --gin-glow: #e2583a;
    --name-ink: #24555b;
    --spirit-ink: #49a3a1;
    --label-text: #ffffff;
    --fruit-peach: #e79a3c;
    --fruit-cran: #b8202c;
  }
  * { margin: 0; padding: 0; box-sizing: border-box; }
  html, body {
    width: 960px;
    height: 1200px;
    overflow: hidden;
    background: var(--page-bg);
  }
  .canvas {
    position: relative;
    width: 960px;
    height: 1200px;
  }
  .label {
    position: absolute;
    left: 210px;
    top: 50px;
    width: 540px;
    height: 1100px;
    overflow: hidden;
    background: linear-gradient(90deg, var(--gin-deep) 0%, var(--gin-red) 30%, var(--gin-glow) 50%, var(--gin-red) 70%, var(--gin-deep) 100%);
  }
  .pattern-band {
    position: absolute;
    left: 0;
    width: 100%;
  }
  .pattern-band--top {
    top: 0;
    height: 360px;
    background: linear-gradient(180deg, var(--teal-light) 0%, var(--teal) 55%, rgba(63,138,138,0) 100%);
  }
  .pattern-band--bottom {
    bottom: 0;
    height: 330px;
    background: linear-gradient(0deg, var(--teal) 0%, var(--teal) 45%, rgba(63,138,138,0) 100%);
  }
  .product-name {
    position: absolute;
    left: 0;
    top: 400px;
    width: 100%;
    text-align: center;
    font-family: "Cormorant Garamond", serif;
    font-weight: 600;
    font-size: 50px;
    line-height: 1.1;
    color: var(--name-ink);
  }
  .spirit {
    position: absolute;
    left: 0;
    top: 470px;
    width: 100%;
    text-align: center;
    font-family: "Cormorant Garamond", serif;
    font-weight: 600;
    font-size: 64px;
    line-height: 1.1;
    letter-spacing: 10px;
    color: var(--spirit-ink);
  }
  .fruit-art {
    position: absolute;
    left: 80px;
    top: 590px;
    width: 380px;
    height: 200px;
    border-radius: 50%;
    background: radial-gradient(ellipse at 60% 45%, var(--fruit-peach) 0%, rgba(231,154,60,0.6) 35%, rgba(184,32,44,0.5) 65%, rgba(184,32,44,0) 80%);
  }
  .volume {
    position: absolute;
    left: 0;
    bottom: 30px;
    width: 100%;
    display: flex;
    justify-content: center;
    gap: 34px;
    font-family: "Open Sans", sans-serif;
    font-weight: 500;
    font-size: 28px;
    color: var(--label-text);
  }
</style>
</head>
<body>
  <main class="canvas">
    <section class="label">
      <div class="pattern-band pattern-band--top" role="img" aria-label="Teal harlequin diamond pattern"></div>
      <div class="pattern-band pattern-band--bottom" role="img" aria-label="Teal harlequin diamond pattern"></div>

      <h1 class="product-name">Cranberry &amp; Peach</h1>
      <p class="spirit">GIN</p>

      <div class="fruit-art" role="img" aria-label="Illustration of peaches, a peach slice and cranberries"></div>

      <p class="volume"><span>50cl</span><span>40% Vol.</span></p>
    </section>
  </main>
</body>
</html>
```